Tallgrove Financial Business Card Design

We are looking for a nice looking business card design. I'd prefer something other than white for the background but white is ok if necessary. I'm uploading two versions of my picture, one is square and one is rounded. Also a couple of versions of the logo for white backgrounds as well as one for darker backgrounds.

Target Market(s)

Realtors and prospective clients

Industry/Entity Type

Mortgage

Contact Information for Business Card

Double sided business card. Not sure what is needed here.

Colors

Designer to choose colors to be used in the design.

Requirements
Must have
• Name: Marcus Ellery
• Title: Senior Mortgage Advisor
• Email: marcusellery@tallgrovefinancial-mail.net
• website: www.marcusellerymortgagecrew-site.com
• Address: 4725 W 860 N, STE 310 Salt Lake City, UT 84199
• Phone: 801-555-0187
• nmls# 482917
• Logo is on our webstie. www.tallgrovefinancial-mail.net
• Picture
Nice to have
• Colors could be similar to our website www.tallgrovefinancial-mail.net
• A list of what we do (VA Loans, FHA Loans, Conventional Loans, USDA Loans)

```html
<!DOCTYPE html>
<html lang="en">
<head>
<meta charset="utf-8">
<title>Tallgrove Financial Business Card</title>
<link rel="stylesheet" href="https://fonts.googleapis.com/css2?family=Roboto:wght@400;500;700&family=Roboto+Condensed:wght@700&display=swap">
<style>
  :root {
    --backdrop: #e9e6e1;
    --card-black: #1b1c1e;
    --card-white: #f3f3f3;
    --band-dark: #222221;
    --ink: #1e1e1e;
    --ink-body: #3a3a3a;
    --ink-muted: #a9a9a9;
    --paper-white: #ffffff;
  }
  * { box-sizing: border-box; margin: 0; padding: 0; }
  html, body { width: 1200px; height: 960px; overflow: hidden; }
  body {
    position: relative;
    background: var(--backdrop);
    font-family: "Roboto", Arial, sans-serif;
  }
  .card {
    position: absolute;
    border-radius: 18px;
    overflow: hidden;
    box-shadow: 0 3px 10px rgba(0,0,0,0.18);
  }
  .card-front {
    left: 320px; top: 108px; width: 590px; height: 345px;
    background: var(--card-black);
    color: var(--paper-white);
  }
  .brand {
    display: flex; align-items: center; gap: 12px;
    font-family: "Roboto", Arial, sans-serif;
    font-weight: 500;
    letter-spacing: 2px;
    text-transform: uppercase;
    white-space: nowrap;
  }
  .brand-mark { display: block; background: currentColor; }
  .card-front .brand {
    position: absolute; left: 0; right: 0; top: 152px;
    justify-content: center;
    font-size: 30px; color: var(--paper-white);
  }
  .card-front .brand-mark { width: 26px; height: 26px; }
  .services {
    position: absolute; left: 0; right: 0; top: 288px;
    text-align: center; font-size: 14.5px; color: var(--paper-white);
    display: flex; justify-content: center; align-items: center; gap: 4px;
  }
  .services .sep { width: 9px; height: 9px; fill: var(--paper-white); }

  .card-back {
    left: 320px; top: 493px; width: 600px; height: 343px;
    background: var(--card-white);
    color: var(--ink-body);
  }
  .side-band {
    position: absolute; left: 0; top: 0; bottom: 0; width: 55px;
    background: var(--band-dark);
  }
  .card-back .brand {
    position: absolute; left: 28px; top: 62px;
    font-size: 28px; color: var(--ink);
  }
  .card-back .brand-mark { width: 24px; height: 24px; }
  .contact-block { position: absolute; left: 91px; top: 140px; }
  .person-name {
    font-family: "Roboto Condensed", "Arial Narrow", sans-serif;
    font-weight: 700; font-size: 21px; color: var(--ink);
    text-transform: uppercase; line-height: 24px;
  }
  .person-title {
    font-size: 14.5px; color: var(--ink-muted); text-transform: uppercase;
    line-height: 20px; margin-bottom: 8px;
  }
  .address { font-size: 14.5px; line-height: 18px; margin-bottom: 8px; }
  .contact-list { list-style: none; font-size: 14.5px; line-height: 19.5px; }
  .contact-list li { display: flex; align-items: center; gap: 9px; }
  .contact-list svg { width: 13px; height: 13px; fill: var(--ink); flex: none; }
</style>
</head>
<body>
  <section class="card card-front" aria-label="Card front">
    <div class="brand"><span class="brand-mark"></span>Tallgrove Financial</div>
    <p class="services">
      <span>VA Loans</span>
      <svg class="sep" viewBox="0 0 10 10"><polygon points="5,0 6.2,3.6 10,3.8 7,6.1 8.1,10 5,7.7 1.9,10 3,6.1 0,3.8 3.8,3.6"/></svg>
      <span>FHA Loans</span>
      <svg class="sep" viewBox="0 0 10 10"><polygon points="5,0 6.2,3.6 10,3.8 7,6.1 8.1,10 5,7.7 1.9,10 3,6.1 0,3.8 3.8,3.6"/></svg>
      <span>Conventional Loans</span>
      <svg class="sep" viewBox="0 0 10 10"><polygon points="5,0 6.2,3.6 10,3.8 7,6.1 8.1,10 5,7.7 1.9,10 3,6.1 0,3.8 3.8,3.6"/></svg>
      <span>USDA Loans</span>
    </p>
  </section>

  <section class="card card-back" aria-label="Card back">
    <div class="side-band"></div>
    <div class="brand"><span class="brand-mark"></span>Tallgrove Financial</div>
    <div class="contact-block">
      <h1 class="person-name">Marcus Ellery</h1>
      <p class="person-title">Senior Mortgage Advisor</p>
      <p class="address">4725 W 860 N, STE 310<br>Salt Lake City, UT 84199<br>nmls# 482917</p>
      <ul class="contact-list">
        <li><svg viewBox="0 0 24 24"><path d="M6.6 10.8c1.4 2.8 3.8 5.1 6.6 6.6l2.2-2.2c.3-.3.7-.4 1-.2 1.1.4 2.3.6 3.6.6.6 0 1 .4 1 1V20c0 .6-.4 1-1 1C10.6 21 3 13.4 3 4c0-.6.4-1 1-1h3.5c.6 0 1 .4 1 1 0 1.3.2 2.5.6 3.6.1.3 0 .7-.2 1z"/></svg>801-555-0187</li>
        <li><svg viewBox="0 0 24 24"><path d="M2 5h20v14H2z M4 7v.5l8 5 8-5V7l-8 5z" fill-rule="evenodd"/></svg>marcusellery@tallgrovefinancial-mail.net</li>
        <li><svg viewBox="0 0 24 24"><circle cx="12" cy="12" r="10"/></svg>marcusellerymortgagecrew-site.com</li>
      </ul>
    </div>
  </section>
</body>
</html>
```